New Website for Corriveld House at www.corriveld.com.au

A new logo has been designed (through pixel forum) and we now want to align the look and feel of our website at www.corriveld.com.au to the new logo. The content and page names (e.g. Grounds) will remain largely unchanged for the new site, so please submit a new look "Home" page, using our new logo, current text and any photos you choose from the existing gallery at our website. I have also attached the current "Home" page photos.

Industry/Entity Type

Accommodation

Number of Pages Required

1 page

Requirements
Must have
• Logo to be presented on white background.

```html
<!DOCTYPE html>
<html lang="en">
<head>
<meta charset="utf-8">
<title>Corriveld House — Home</title>
<link href="https://fonts.googleapis.com/css2?family=Crimson+Pro:ital,wght@0,400;0,600;1,400;1,600;1,700&display=swap" rel="stylesheet">
<style>
  :root {
    --white: #ffffff;
    --ink: #555555;
    --ink-dark: #3b3b3b;
    --brand-blue: #0aa0dc;
    --sun-yellow: #fedf55;
    --slate: #4b4b4b;
    --charcoal: #3a3a3a;
    --rule: #d9d9d9;
  }
  * { margin: 0; padding: 0; box-sizing: border-box; }
  html, body { width: 822px; height: 1200px; overflow: hidden; background: var(--white); }
  body { position: relative; font-family: "Crimson Pro", Georgia, serif; color: var(--ink); }
  .abs { position: absolute; }

  /* Header */
  .site-header { left: 0; top: 0; width: 822px; height: 99px; background: var(--white); }
  .brand { left: 0; top: 36px; width: 822px; display: flex; justify-content: center; align-items: center; gap: 8px; }
  .brand-dot { width: 14px; height: 14px; border-radius: 50%; background: var(--sun-yellow); }
  .brand-name { font-size: 26px; font-weight: 400; color: var(--brand-blue); letter-spacing: 0.5px; }

  .main-nav { left: 0; top: 99px; width: 822px; height: 31px; border-top: 1px solid var(--rule); background: var(--white); }
  .nav-item { top: 8px; font-size: 9px; letter-spacing: 0.3px; color: var(--ink); transform: translateX(-50%); white-space: nowrap; }

  /* Hero */
  .hero { left: 0; top: 130px; width: 822px; height: 340px;
    background: linear-gradient(180deg, #2c2c2c 0%, #3e3e3e 45%, #555 75%, #3a3a3a 100%); }
  .hero-kicker { left: 0; top: 124px; width: 822px; text-align: center; font-size: 12px; letter-spacing: 10px; color: var(--sun-yellow); }
  .hero-title { left: 0; top: 148px; width: 822px; text-align: center; font-size: 37px; letter-spacing: 5px; color: var(--white); font-weight: 400; }
  .hero-lede { left: 240px; top: 201px; width: 342px; text-align: center; font-size: 8px; line-height: 17px; color: #c9c9c9; }

  /* Welcome */
  .welcome-rule { top: 534px; height: 1px; width: 69px; background: #bdbdbd; }
  .welcome-title { left: 0; top: 521px; width: 822px; text-align: center; font-size: 19px; font-style: italic; color: var(--ink); }
  .welcome-sub { left: 0; top: 566px; width: 822px; text-align: center; font-size: 12.5px; color: var(--brand-blue); }
  .welcome-copy { left: 140px; top: 597px; width: 542px; text-align: center; font-size: 9.6px; line-height: 17.2px; color: var(--ink); }
  .welcome-copy a { color: var(--brand-blue); font-weight: 600; text-decoration: none; }
  .btn { top: 686px; width: 88px; height: 27px; border-radius: 2px; font-size: 10px; font-style: italic; font-weight: 700;
    display: flex; align-items: center; justify-content: center; }
  .btn-solid { left: 318px; background: var(--brand-blue); color: var(--white); }
  .btn-outline { left: 416px; border: 1px solid var(--brand-blue); color: var(--brand-blue); }

  /* Testimonial */
  .testimonial { left: 0; top: 753px; width: 411px; height: 226px; background: var(--slate); }
  .quote-mark { left: 96px; top: 808px; font-size: 34px; font-weight: 700; color: var(--sun-yellow); line-height: 1; }
  .quote-text { left: 130px; top: 817px; width: 225px; font-size: 9.8px; line-height: 17.2px; font-style: italic; font-weight: 700; color: var(--white); }
  .quote-cite { left: 131px; top: 907px; font-size: 9.5px; color: var(--sun-yellow); font-weight: 600; }
  .quote-cite span { font-size: 8px; font-weight: 400; margin-left: 3px; }
  .estate-photo { left: 411px; top: 753px; width: 411px; height: 226px;
    background: linear-gradient(160deg, #5f8a4a 0%, #c8794f 28%, #d9cfb2 50%, #4fb0c6 62%, #3d6b35 85%, #7a7a5c 100%); }

  /* Info band */
  .info-band { left: 0; top: 979px; width: 822px; height: 175px; background: var(--sun-yellow); }
  .info-heading { top: 1014px; font-size: 8.5px; font-weight: 600; color: var(--ink-dark); letter-spacing: 0.2px; }
  .info-divider { top: 1038px; width: 1px; height: 41px; background: #e2c23c; }
  .address { left: 96px; top: 1035px; font-size: 12.5px; line-height: 17.2px; color: var(--ink-dark); }
  .call-line { left: 350px; top: 1035px; font-size: 12.5px; color: var(--ink-dark); }
  .phone { left: 349px; top: 1054px; font-size: 19px; color: var(--ink-dark); letter-spacing: 0.5px; }
  .btn-availability { left: 351px; top: 1088px; width: 119px; height: 28px; border: 1.5px solid var(--ink-dark);
    display: flex; align-items: center; justify-content: center; font-size: 9.5px; color: var(--ink-dark); }
  .social-list { left: 567px; top: 1040px; display: flex; gap: 3px; }
  .social-dot { width: 18px; height: 18px; border-radius: 50%; border: 1.3px solid var(--ink-dark); }

  /* Footer bar */
  .site-footer { left: 0; top: 1154px; width: 822px; height: 46px; background: var(--charcoal);
    font-family: Arial, Helvetica, sans-serif; font-size: 8px; color: #c4c4c4; }
  .copyright { left: 96px; top: 17px; }
  .footer-links { right: 95px; top: 17px; }
  .footer-links .sep { margin: 0 4px; }
</style>
</head>
<body>

<header class="abs site-header">
  <div class="abs brand">
    <span class="brand-dot"></span>
    <span class="brand-name">Corriveld House</span>
  </div>
</header>

<nav class="abs main-nav">
  <span class="abs nav-item" style="left:137px">HOME</span>
  <span class="abs nav-item" style="left:206px">EXPLORE</span>
  <span class="abs nav-item" style="left:276px">GALLARY</span>
  <span class="abs nav-item" style="left:345px">ROOM</span>
  <span class="abs nav-item" style="left:429px">AVILIABILITY</span>
  <span class="abs nav-item" style="left:522px">LOCATION</span>
  <span class="abs nav-item" style="left:606px">CONTACT</span>
  <span class="abs nav-item" style="left:680px">OPTIONS</span>
</nav>

<section class="abs hero" role="img" aria-label="Aerial photo of the mansion with tiled roofs and arched verandah, surrounded by tall trees">
  <p class="abs hero-kicker">STAY WITH US</p>
  <h1 class="abs hero-title">FEEL LIKE HOME</h1>
  <p class="abs hero-lede">Lorem Ipsum is simply dummy text of the printing and typesetting industry. Lorem Ipsum has been the industry's standard dummy text</p>
</section>

<section class="welcome">
  <span class="abs welcome-rule" style="left:216px"></span>
  <h2 class="abs welcome-title">Welcome To Corriveld House</h2>
  <span class="abs welcome-rule" style="left:539px"></span>
  <h3 class="abs welcome-sub" style="font-weight:400">PALATIAL ESTATE AND LUXURY RESORT</h3>
  <p class="abs welcome-copy">On over 2 manicured garden acres, Corriveld House is a unique Gold Coast estate, centrally located in the prestigious rural suburb of Bellmere Ridge. <a href="#">More about our Location</a>.&nbsp; The estate features a grand mansion, private pub (The Heron and Reed), sparkling resort pool, tennis court and playground.&nbsp; Magnificent properties rarely feel so warm and welcoming – so browse away and visit our <a href="#">photo gallery</a> – and we look forward to having you stay as our guests. For prices, availability and guest reviews, visit <a href="#">StayNest</a>.</p>
  <a class="abs btn btn-solid">Take a tour</a>
  <a class="abs btn btn-outline">Start Booking</a>
</section>

<section class="abs testimonial"></section>
<span class="abs quote-mark">“</span>
<blockquote class="abs quote-text">Lorem Ipsum is simply dummy text of the printing and typesetting industry. Lorem Ipsum has been the industry's standard dummy text ever since the 1500s, when an unknown</blockquote>
<p class="abs quote-cite">Jane Marlow,<span>Northwind</span></p>
<div class="abs estate-photo" role="img" aria-label="Aerial view of the house with terracotta roofs, pool and palm trees"></div>

<section class="abs info-band"></section>
<h4 class="abs info-heading" style="left:96px">OUR ADDRESS</h4>
<address class="abs address" style="font-style:normal">24 Wattlebird Drive<br>Bellmere Ridge, Gold Coast, Greenland<br>Australia.</address>
<span class="abs info-divider" style="left:290px"></span>
<h4 class="abs info-heading" style="left:350px">CONTACT US</h4>
<p class="abs call-line">Call us for reservation at</p>
<p class="abs phone">00 55501 55501</p>
<a class="abs btn-availability">Check Avilaibility</a>
<span class="abs info-divider" style="left:532px"></span>
<h4 class="abs info-heading" style="left:568px">SOCIAL LINKS</h4>
<div class="abs social-list" aria-label="Social links">
  <span class="social-dot"></span><span class="social-dot"></span><span class="social-dot"></span><span class="social-dot"></span><span class="social-dot"></span>
</div>

<footer class="abs site-footer">
  <span class="abs copyright">© 2016 Corriveld House. All Rights Reserved.</span>
  <span class="abs footer-links">Home<span class="sep">|</span>Aboout<span class="sep">|</span>Booking<span class="sep">|</span>Location<span class="sep">|</span>Contact</span>
</footer>

</body>
</html>
```